Stationary and Business Cards
Bright Harbor Legal
Project: Stationary and Business Cards
Stationary and Business Cards - Law
Creative Brief
Professional
Marek Vandellin
Director Of Operations
412 Willowmere Cres Toronto, Ontario M4R 7J9
Marek@brightharborlegal-example.ca
brightharborlegal-example.ca
Serving the Greater Toronto Area region.
Our goal is to provide our customers with outstanding service through dedication and excellence and to ensure we are the industry leader. Our charges will be fair, competitive and driven by our level of effort expanded.

```html
<!DOCTYPE html>
<html lang="en">
<head>
<meta charset="utf-8">
<title>Bright Harbor Legal — Stationery Set</title>
<link href="https://fonts.googleapis.com/css2?family=Roboto+Condensed:wght@400;700&family=Open+Sans:wght@400;600&display=swap" rel="stylesheet">
<style>
  :root{
    --bg:#e4e1dc;
    --paper:#ffffff;
    --ink:#1b1b1b;
    --dark-1:#3a3a3a;
    --dark-2:#151515;
    --red:#c8161b;
    --line:#b9b9b9;
  }
  *{box-sizing:border-box;margin:0;padding:0}
  html,body{width:1200px;height:600px;overflow:hidden;background:var(--bg)}
  body{position:relative;font-family:"Open Sans",sans-serif;color:var(--ink)}

  .sheet{position:absolute;background:var(--paper);box-shadow:0 3px 10px rgba(0,0,0,.25);overflow:hidden}
  .letterhead{left:67px;top:84px;width:334px;height:449px}
  .fax-sheet{left:425px;top:84px;width:336px;height:449px}

  .band{position:absolute;left:0;right:0;background:linear-gradient(180deg,var(--dark-1),var(--dark-2))}
  .band--head{top:0;height:40px}
  .band--foot{bottom:0;height:36px}

  .brand{position:absolute;display:flex;align-items:center;gap:6px}
  .brand__mark{width:16px;height:16px;border-radius:50%;background:var(--red);flex:none}
  .brand__text{display:flex;flex-direction:column;line-height:1}
  .brand__name{font-family:"Roboto Condensed",sans-serif;font-weight:700;font-size:10px;color:#fff;text-transform:uppercase;letter-spacing:.3px;white-space:nowrap}
  .brand__tag{font-size:4.5px;color:#cfcfcf;margin-top:2px;white-space:nowrap}
  .band--head .brand{left:12px;top:12px}
  .head-web{position:absolute;right:12px;top:24px;font-size:5px;color:#ddd}

  .accent-block{position:absolute;background:var(--red)}
  .band--foot .accent-block{left:0;top:0;bottom:0;width:16px}
  .foot-info{position:absolute;left:30px;bottom:12px;font-size:4.6px;color:#e0e0e0;line-height:1.5}
  .foot-web{position:absolute;right:12px;bottom:8px;font-size:4.6px;color:#e0e0e0}
  .foot-mark{position:absolute;right:80px;bottom:9px;width:16px;height:16px;border-radius:50%;background:var(--red)}

  .fax-title{position:absolute;left:14px;top:64px;font-size:22px;font-weight:400;letter-spacing:1px}
  .fax-fields{position:absolute;left:14px;top:100px;width:306px;display:grid;grid-template-columns:1fr 1fr;column-gap:14px;row-gap:7px}
  .fax-field{font-size:5.5px;border-bottom:1px solid var(--line);padding-bottom:2px;color:#444}
  .fax-rule{position:absolute;left:14px;top:168px;width:306px;border-top:1.5px solid #555}
  .fax-checks{position:absolute;left:14px;top:176px;display:flex;gap:16px;font-size:5.5px;color:#444}
  .fax-check{display:flex;align-items:center;gap:3px}
  .fax-check::before{content:"";width:6px;height:6px;border:1px solid #777}

  .card{position:absolute;top:103px;width:146px;height:82px;box-shadow:0 3px 8px rgba(0,0,0,.3);overflow:hidden;background:linear-gradient(160deg,var(--dark-1),var(--dark-2))}
  .card--front{left:804px}
  .card--back{left:965px}
  .card .brand__name{font-size:8.5px}
  .card .brand__mark{width:13px;height:13px}
  .card--front .accent-block{right:0;top:0;bottom:0;width:12px}
  .card--front .brand{left:8px;top:10px}
  .card-person{position:absolute;left:27px;top:32px;font-size:4.8px;color:#ddd;line-height:1.5}
  .card-person strong{font-family:"Roboto Condensed",sans-serif;font-size:6.5px;color:#fff;font-weight:700}
  .card-contact{position:absolute;left:27px;bottom:8px;font-size:4.2px;color:#ccc;line-height:1.5;white-space:nowrap}
  .card--back .accent-block{right:0;top:0;bottom:0;width:26px}
  .card--back .brand{left:12px;top:34px}
  .card-back-web{position:absolute;left:12px;bottom:8px;font-size:4.5px;color:#fff}

  .envelope{left:806px;width:329px}
  .envelope--front{top:211px;height:166px}
  .envelope--front .band--head{height:22px}
  .envelope--front .brand{left:10px;top:3px}
  .env-web{position:absolute;right:10px;top:8px;font-size:4.5px;color:#ddd}
  .env-return{position:absolute;left:10px;bottom:10px;font-size:4.2px;color:#888}
  .envelope--back{top:384px;height:150px}
  .env-flap{position:absolute;left:0;top:0}
  .env-back-info{position:absolute;left:0;right:0;top:8px;text-align:center;font-size:4.2px;color:#555}
</style>
</head>
<body>

<section class="sheet letterhead" aria-label="Letterhead">
  <div class="band band--head">
    <div class="brand"><span class="brand__mark"></span><span class="brand__text"><span class="brand__name">Bright Harbor Legal</span><span class="brand__tag">Serving the Greater Toronto Area</span></span></div>
    <span class="head-web">brightharborlegal-example.ca</span>
  </div>
  <div class="band band--foot">
    <div class="accent-block" role="img" aria-label="Red decorative accent"></div>
    <div class="foot-info">412 Willowmere Cres Toronto, Ontario M4R 7J9<br>T: 416-555-0142 &nbsp; F: 416-555-0143</div>
    <span class="foot-mark"></span>
    <span class="foot-web">brightharborlegal-example.ca</span>
  </div>
</section>

<section class="sheet fax-sheet" aria-label="Fax cover sheet">
  <div class="band band--head">
    <div class="brand"><span class="brand__mark"></span><span class="brand__text"><span class="brand__name">Bright Harbor Legal</span><span class="brand__tag">Serving the Greater Toronto Area</span></span></div>
    <span class="head-web">brightharborlegal-example.ca</span>
  </div>
  <h1 class="fax-title">FAX</h1>
  <div class="fax-fields">
    <span class="fax-field">To:</span><span class="fax-field">From:</span>
    <span class="fax-field">Fax:</span><span class="fax-field">Pages:</span>
    <span class="fax-field">Phone:</span><span class="fax-field">Date:</span>
    <span class="fax-field">Re:</span><span class="fax-field">CC:</span>
  </div>
  <div class="fax-rule"></div>
  <div class="fax-checks">
    <span class="fax-check">Urgent</span><span class="fax-check">For Review</span><span class="fax-check">Please Comment</span><span class="fax-check">Please Reply</span><span class="fax-check">Please Recycle</span>
  </div>
  <div class="band band--foot">
    <div class="accent-block" role="img" aria-label="Red decorative accent"></div>
    <div class="foot-info">412 Willowmere Cres Toronto, Ontario M4R 7J9<br>T: 416-555-0142 &nbsp; F: 416-555-0143</div>
    <span class="foot-mark"></span>
    <span class="foot-web">brightharborlegal-example.ca</span>
  </div>
</section>

<section class="card card--front" aria-label="Business card front">
  <div class="accent-block" role="img" aria-label="Red decorative accent"></div>
  <div class="brand"><span class="brand__mark"></span><span class="brand__text"><span class="brand__name">Bright Harbor Legal</span></span></div>
  <div class="card-person"><strong>Marek Vandellin</strong><br>Director Of Operations</div>
  <div class="card-contact">T: 416-555-0142<br>Marek@brightharborlegal-example.ca<br>412 Willowmere Cres Toronto, Ontario M4R 7J9</div>
</section>

<section class="card card--back" aria-label="Business card back">
  <div class="accent-block" role="img" aria-label="Red decorative accent"></div>
  <div class="brand"><span class="brand__mark"></span><span class="brand__text"><span class="brand__name">Bright Harbor Legal</span></span></div>
  <span class="card-back-web">brightharborlegal-example.ca</span>
</section>

<section class="sheet envelope envelope--front" aria-label="Envelope front">
  <div class="band band--head">
    <div class="brand"><span class="brand__mark"></span><span class="brand__text"><span class="brand__name">Bright Harbor Legal</span></span></div>
    <span class="env-web">brightharborlegal-example.ca</span>
  </div>
  <div class="env-return">412 Willowmere Cres Toronto, Ontario M4R 7J9</div>
</section>

<section class="sheet envelope envelope--back" aria-label="Envelope back">
  <svg class="env-flap" width="329" height="150" viewBox="0 0 329 150">
    <defs><linearGradient id="flapShade" x1="0" y1="0" x2="0" y2="1"><stop offset="0" stop-color="#3a3a3a"/><stop offset="1" stop-color="#151515"/></linearGradient></defs>
    <path d="M0 28 L329 28 L329 40 L164.5 100 L0 40Z" fill="url(#flapShade)"/>
    <circle cx="164.5" cy="92" r="9" fill="var(--red)"/>
  </svg>
  <div class="env-back-info">412 Willowmere Cres Toronto, Ontario M4R 7J9 &nbsp; T: 416-555-0142</div>
</section>

</body>
</html>
```